Home Page Design

We have a B2B home page design and need a consumer version. The look and feel can look similar but needs to be distinctly different so it in not to get confused. Essentially it should look like the same company with a different model. We will need a PSD w all layers organized and easy to understand. Attached is the logo, B2B comp, and a MS Word doc with a short description. In addition, I have attached a wire frame to be used as a site map. PLEASE DO NOT take that as the creative. I expect to see your creative based on the information provided.

Consumer

```html
<!DOCTYPE html>
<html lang="en">
<head>
<meta charset="utf-8">
<title>GiveHost.com — Home</title>
<link rel="stylesheet" href="https://fonts.googleapis.com/css2?family=Lato:ital,wght@0,400;0,700;0,900;1,400;1,700&display=swap">
<style>
:root{
  --blue:#1b6c98;
  --blue-dark:#155a80;
  --green:#3bb14a;
  --text:#2b2b2b;
  --muted:#6b6b6b;
  --line:#b9b9b9;
  --field-border:#c9c9c9;
  --bg:#ffffff;
}
*{box-sizing:border-box;margin:0;padding:0}
html,body{width:1200px;height:938px;overflow:hidden;background:var(--bg);font-family:"Lato",Arial,sans-serif;color:var(--text)}
.page{position:relative;width:1200px;height:938px}

.brand{position:absolute;left:132px;top:26px;display:flex;align-items:center;gap:14px}
.brand-dot{width:66px;height:66px;border-radius:50%;background:var(--blue)}
.brand-name{font-size:33px;font-weight:400;color:var(--green)}

.main-nav{position:absolute;top:57px;left:561px;display:flex;align-items:center}
.main-nav a{font-size:16px;font-weight:700;color:var(--text);text-decoration:none;white-space:nowrap}
.nav-cta{background:var(--blue);color:#fff !important;padding:4px 9px;border-radius:2px;width:125px;text-align:center}
.nav-auction{margin-left:34px}
.nav-about{margin-left:40px}
.nav-contact{margin-left:44px}

.hero{position:absolute;left:132px;top:111px;width:938px;height:299px;border-radius:6px;overflow:hidden;
  background:linear-gradient(180deg,#c9d3d8 0%,#a9b8be 22%,#6f8f56 42%,#5f8a3a 65%,#4c7430 100%);
  box-shadow:0 14px 14px -8px rgba(0,0,0,.35)}
.hero-caption{position:absolute;left:476px;top:180px;font-size:29px;font-style:italic;font-weight:700;line-height:37px;color:#fff;text-shadow:0 1px 3px rgba(0,0,0,.35)}
.hero-dots{position:absolute;top:430px;left:561px;display:flex;gap:7px}
.hero-dots span{width:14px;height:14px;border-radius:50%;background:#9a9a9a}
.hero-dots .active{background:var(--green);box-shadow:0 0 0 2px #cfe9d2}

.section-title{position:absolute;display:flex;align-items:center;gap:14px;font-size:18px;font-weight:700;color:var(--blue)}
.section-title::before{content:"";width:29px;height:29px;border-radius:50%;background:var(--blue)}
.rule{position:absolute;height:0;border-top:2px dotted var(--line)}

.card-row{position:absolute;left:133px;display:flex;gap:15px}
.card{width:150px;height:121px;background:#fff;box-shadow:0 3px 6px rgba(0,0,0,.22)}
.card-label{height:38px;background:var(--blue);color:#fff;font-size:13.5px;font-weight:700;line-height:15px;text-align:center;display:flex;align-items:center;justify-content:center;padding:0 4px}
.card-photo{margin:7px 8px 0;height:70px}

.search-form{position:absolute;left:800px;width:270px}
.field{display:block;width:270px;height:24px;margin-bottom:8px;border:1px solid var(--field-border);border-radius:3px;padding:0 12px;font-size:12px;font-style:italic;line-height:22px;color:#555;background:#fff}
.btn-search{display:inline-block;margin-top:2px;width:74px;height:24px;background:var(--green);color:#fff;font-size:15px;font-weight:700;text-align:center;line-height:24px;border-radius:2px}

.site-footer{position:absolute;left:0;top:900px;width:1200px;height:30px;background:var(--blue);color:#fff;font-size:13px;font-weight:700}
.site-footer::after{content:"";position:absolute;left:0;top:30px;width:1200px;height:8px;background:var(--green)}
.footer-nav{position:absolute;left:132px;top:7px}
.footer-mark{position:absolute;left:648px;top:3px;width:24px;height:24px;border-radius:50%;background:#6fa5c3}
.copyright{position:absolute;right:130px;top:7px}
</style>
</head>
<body>
<div class="page">
  <header>
    <div class="brand"><span class="brand-dot"></span><span class="brand-name">GiveHost.com</span></div>
    <nav class="main-nav">
      <a class="nav-cta" href="#">Post Your Event</a>
      <a class="nav-auction" href="#">Add Auction Items</a>
      <a class="nav-about" href="#">About Us</a>
      <a class="nav-contact" href="#">Contact Us</a>
    </nav>
  </header>

  <section class="hero" role="img" aria-label="Golfers walking a green seaside golf course above ocean cliffs">
    <p class="hero-caption">Lorem ipsum dolor sit amet consect<br>etuer adipiscing elit</p>
  </section>
  <div class="hero-dots"><span class="active"></span><span></span><span></span><span></span></div>

  <h2 class="section-title" style="left:135px;top:470px">Featured Auction Items</h2>
  <div class="rule" style="left:132px;top:505px;width:629px"></div>
  <div class="card-row" style="top:525px">
    <article class="card"><div class="card-label">Dinner With<br>Marcus Bell</div><div class="card-photo" role="img" aria-label="Guests at a formal dinner" style="background:linear-gradient(135deg,#5a1f1f,#b3352f 55%,#2a1a18)"></div></article>
    <article class="card"><div class="card-label">Case of<br>Valle Rosa Wine</div><div class="card-photo" role="img" aria-label="Glass of white wine beside a bottle on a table" style="background:linear-gradient(135deg,#6b5d45,#c9b58a 50%,#8a7a5a)"></div></article>
    <article class="card"><div class="card-label">Ridgeway<br>Bicycle</div><div class="card-photo" role="img" aria-label="Racing bicycle on a dark background" style="background:radial-gradient(circle at 50% 55%,#a06a2a,#3a2410 55%,#120c06)"></div></article>
    <article class="card"><div class="card-label">5 Days/4 Nights<br>in Paris France</div><div class="card-photo" role="img" aria-label="Glass pyramid museum lit at dusk in Paris" style="background:linear-gradient(180deg,#4a3a5a,#c98a3a 60%,#6a4522)"></div></article>
  </div>

  <h2 class="section-title" style="left:800px;top:470px">Search For An Auction Item</h2>
  <div class="rule" style="left:800px;top:505px;width:270px"></div>
  <form class="search-form" style="top:525px">
    <span class="field">Auction Type</span>
    <span class="field">Auction Date</span>
    <span class="field">Charity</span>
    <span class="btn-search">Search</span>
  </form>

  <h2 class="section-title" style="left:135px;top:676px">Featured Golf Event</h2>
  <div class="rule" style="left:132px;top:711px;width:629px"></div>
  <div class="card-row" style="top:732px">
    <article class="card"><div class="card-label">November 12<br>Riverbend County Club</div><div class="card-photo" role="img" aria-label="Clubhouse building behind a green lawn" style="background:linear-gradient(180deg,#9fc3e0,#e8e2d4 45%,#5f9a3e)"></div></article>
    <article class="card"><div class="card-label">November 16<br>Harbor Dunes</div><div class="card-photo" role="img" aria-label="Dune golf course fairway" style="background:linear-gradient(180deg,#b8c8cf,#7a9a5a 40%,#4f7a32)"></div></article>
    <article class="card"><div class="card-label">November 18<br>Bayside Links</div><div class="card-photo" role="img" aria-label="Aerial view of an island green surrounded by water" style="background:radial-gradient(circle at 50% 55%,#6fa84a,#2f6a7a 45%,#1e3f4a)"></div></article>
    <article class="card"><div class="card-label">November 19<br>Costa Verde</div><div class="card-photo" role="img" aria-label="Resort pool lit at dusk" style="background:linear-gradient(180deg,#3a4a7a,#c98a4a 45%,#2a8ab0)"></div></article>
  </div>

  <h2 class="section-title" style="left:800px;top:676px">Search for Golf Event</h2>
  <div class="rule" style="left:800px;top:711px;width:270px"></div>
  <form class="search-form" style="top:732px">
    <span class="field">Event Type</span>
    <span class="field">Event Date</span>
    <span class="field">Event Location</span>
    <span class="field">Event Name</span>
    <span class="btn-search">Search</span>
  </form>

  <footer class="site-footer">
    <div class="footer-nav">Post Your Event &nbsp;|&nbsp; Add Auction Items &nbsp;|&nbsp; About Us &nbsp;|&nbsp; Contact Us</div>
    <span class="footer-mark"></span>
    <div class="copyright">©2014 GiveHost. All Rights Reserved.</div>
  </footer>
</div>
</body>
</html>
```